Business Card Design

i am looking a business card for a car rental company long with Taxi service also a logo.
Updates

what is the latest with my project

Industry/Entity Type

Business

Contact Information for Business Card

name of the Company is Brenmoor Auto Hire and Cab Services
Address: Marlow Bay Village, St. Corin's Parish Antigua
Tele# 558-2047/6194852-613-9075
Email: tolvipark@quenmail.net

Font styles to use
Script

```html
<!DOCTYPE html>
<html lang="en">
<head>
<meta charset="utf-8">
<title>Brenmoor Auto Hire and Cab Services – Business Card</title>
<link href="https://fonts.googleapis.com/css2?family=Arimo:wght@400;700&display=swap" rel="stylesheet">
<style>
  :root {
    --page-bg: #e9eaec;
    --card-blue-light: #6b9dd0;
    --card-blue-dark: #4677b5;
    --card-white: #f4f4f4;
    --card-white-edge: #e3e3e3;
    --text-light: #ffffff;
    --text-dark: #1c1c1c;
    --mark-orange: #f39a12;
    --card-shadow: rgba(0, 0, 0, 0.18);
  }
  * { box-sizing: border-box; margin: 0; padding: 0; }
  html, body {
    width: 1200px;
    height: 1000px;
    overflow: hidden;
    background: var(--page-bg);
    font-family: "Arimo", Arial, sans-serif;
  }
  .sheet {
    position: relative;
    width: 1200px;
    height: 1000px;
  }
  .card {
    position: absolute;
    left: 250px;
    width: 700px;
    height: 400px;
    box-shadow: 0 10px 30px var(--card-shadow);
    overflow: hidden;
  }
  .card--front { top: 70px; display: flex; }
  .card--back {
    top: 530px;
    background: linear-gradient(135deg, var(--card-blue-light) 0%, var(--card-blue-dark) 100%);
  }

  /* Front: contact panel */
  .contact-panel {
    width: 390px;
    height: 100%;
    background: linear-gradient(160deg, var(--card-blue-dark) 0%, var(--card-blue-light) 100%);
    color: var(--text-light);
    padding: 76px 0 0 56px;
  }
  .cardholder-name {
    font-weight: 700;
    font-size: 21px;
    line-height: 1.2;
  }
  .cardholder-role {
    font-size: 16px;
    margin-top: 4px;
  }
  .contact-list {
    list-style: none;
    margin-top: 62px;
    font-size: 16px;
    line-height: 1.4;
  }
  .contact-list .address { margin-bottom: 8px; }
  .contact-list .address span { display: block; }
  .contact-list li + li { margin-top: 6px; }

  /* Front: brand panel */
  .brand-panel {
    flex: 1;
    background: linear-gradient(180deg, var(--card-white) 0%, var(--card-white-edge) 100%);
    display: flex;
    flex-direction: column;
    align-items: center;
    justify-content: center;
    padding: 0 30px;
  }
  .brand-dot {
    width: 56px;
    height: 56px;
    border-radius: 50%;
    background: var(--mark-orange);
    margin-bottom: 20px;
  }
  .brand-name {
    font-size: 22px;
    font-weight: 400;
    text-align: center;
    line-height: 1.3;
    color: var(--text-dark);
  }

  /* Back */
  .back-brand {
    position: absolute;
    inset: 0;
    display: flex;
    flex-direction: column;
    align-items: center;
    justify-content: center;
    padding: 0 140px;
  }
  .back-brand .brand-dot { width: 70px; height: 70px; margin-bottom: 24px; }
  .back-brand .brand-name { color: var(--text-light); font-size: 30px; }
</style>
</head>
<body>
  <main class="sheet">
    <section class="card card--front" aria-label="Business card front">
      <div class="contact-panel">
        <p class="cardholder-name">Cardholder Name</p>
        <p class="cardholder-role">Designation</p>
        <ul class="contact-list">
          <li class="address"><span>Marlow Bay Village,</span><span>St. Corin's Parish Antigua</span></li>
          <li class="phone">p: 558-2047/6194852-613-9075</li>
          <li class="email">e: tolvipark@quenmail.net</li>
        </ul>
      </div>
      <div class="brand-panel">
        <span class="brand-dot" aria-hidden="true"></span>
        <p class="brand-name">Brenmoor Auto Hire and Cab Services</p>
      </div>
    </section>

    <section class="card card--back" aria-label="Business card back">
      <div class="back-brand">
        <span class="brand-dot" aria-hidden="true"></span>
        <p class="brand-name">Brenmoor Auto Hire and Cab Services</p>
      </div>
    </section>
  </main>
</body>
</html>
```